Skyvanterra.com

My website is a kind of blog, about drones and UAVs. Now I want to add another part where A guite to UAV/Drone companies will show up and ad space will be needed. I have now, name and address of many, maybe most of such a companies. What I'd like is a new page design for this purpose. I hope I let me understood.
Updates

Hello Designers. I think that none of you have understood what I asked for. What I want is a Drone-Directory Template page which be added to SkyvanTerra.com on a WP base. Anyone of you has viewed a Bluefern Listing Book? Well that is what I want. An elegant Directory web page. I'll put on the page drone manufacturers name, address, email and one or many ads as you've seen on a Bluefern Listings Book. Don't forget that this page will be used as a WP Template. Regards Marcello

Hi, I would like to extend this project for one more week since none of designers undestood what I want althogh I've sent messages clarifying to some of them. Please tell me what next steps will be.

Reason: I would like to extend deadline for 7 more days. Once accepted by designers, I will explain them again what is what I want.

Target Market(s)

Customers will be people engaged in the drine business. Ages 19-65. Mos of the will be English speaking. Most of them own drone manufacture pr drone distribution business.
People liking speed, photography, farming, rescue, investigation and so on.

Font styles to use
Serif
Sans Serif

Requirements
Must have
• Think it is a guide. There should be lines, an abc... Too. And also think that, as any other guide, there will be people interested in shoeing up more by means of advertisements. So,lace for ads are a must.
Nice to have
• Logo ahould show a flying srone
Should not have
• Not old style.Modern fonts, no money bag illustrations.

```html
<!DOCTYPE html>
<html lang="en">
<head>
<meta charset="utf-8">
<title>Drone Directory</title>
<link rel="stylesheet" href="https://fonts.googleapis.com/css2?family=Open+Sans:wght@400;600;700&family=Oswald:wght@500&display=swap">
<style>
:root{
  --yellow:#f5c400;
  --ink:#222;
  --dark:#1b1b1b;
  --charcoal:#333;
  --grey:#666;
  --light:#f1f1f1;
  --line:#e2e2e2;
  --white:#fff;
}
*{margin:0;padding:0;box-sizing:border-box}
html,body{width:1080px;height:1200px;overflow:hidden}
body{position:relative;background:var(--white);font-family:"Open Sans",Arial,sans-serif;color:var(--ink);font-size:9px}
.abs{position:absolute}
/* header */
.topbar{left:0;top:0;width:1080px;height:36px;background:var(--white)}
.brand{left:214px;top:7px;font-size:17px;color:var(--grey);letter-spacing:.2px}
.top-links{left:622px;top:12px;display:flex;gap:18px;font-size:8px;color:var(--grey);align-items:center}
.top-links span::before{content:"";display:inline-block;width:8px;height:8px;border-radius:50%;background:#999;margin-right:5px;vertical-align:-1px}
.add-listing{left:782px;top:6px;width:66px;height:21px;background:var(--charcoal);color:var(--yellow);font-size:8px;font-weight:700;display:flex;align-items:center;justify-content:center}
.add-listing b{color:var(--yellow);margin-right:4px}
/* hero */
.hero{left:0;top:36px;width:1080px;height:350px;background:linear-gradient(180deg,#2a2a2a 0%,#4a3f35 45%,#3a3430 100%)}
.search-strip{left:0;top:36px;width:1080px;height:32px;background:#1e1e1e}
.search-row{left:214px;top:43px;width:634px;height:19px;display:flex;gap:1px}
.search-row .menu{width:23px;background:var(--white);display:flex;flex-direction:column;justify-content:center;align-items:center;gap:2px}
.search-row .menu i{display:block;width:9px;height:1.5px;background:#555}
.search-row .field{flex:1;background:var(--white);color:#aaa;font-size:7.5px;padding:5px 6px}
.search-row .go{width:24px;background:var(--yellow)}
.alpha{left:214px;top:70px;width:634px;height:20px;background:var(--yellow);display:flex;justify-content:space-around;align-items:center;padding:0 20px;font-size:8px;font-weight:600}
.alpha span{width:14px;text-align:center;line-height:20px}
.alpha .on{background:var(--charcoal);color:var(--white)}
.hero-title{left:0;top:136px;width:1080px;text-align:center;color:var(--white);font-size:30px;font-weight:400}
.hero-sub{left:0;top:176px;width:1080px;text-align:center;color:var(--white);font-size:10px;font-weight:700}
/* nav */
.nav{left:214px;top:253px;width:634px;height:27px;background:var(--white);border-bottom:3px solid var(--yellow);display:flex;font-size:8px;font-weight:700}
.nav a{padding:0 15px;line-height:24px;color:var(--ink);text-decoration:none}
.nav a.on{background:var(--yellow)}
.panel{left:214px;top:280px;width:634px;height:416px;background:var(--white)}
/* sidebar */
.side-head{left:214px;top:298px;width:154px;height:30px;background:var(--charcoal);color:var(--white);font-size:9px;padding:10px 11px}
.side-list{left:214px;top:330px;width:154px;list-style:none}
.side-list li{height:21px;line-height:21px;padding-left:11px;font-size:8px;background:var(--light);border-bottom:1px solid var(--white)}
.side-list li.first{background:var(--white);border-left:2px solid var(--yellow);padding-left:9px}
.see-more{left:225px;top:522px;font-size:8px;font-weight:700}
.side-ad{left:214px;top:556px;width:154px;height:72px;background:#1d3557;color:var(--white);text-align:center;padding-top:14px}
.side-ad .t1{font-size:11px;font-weight:700;color:var(--yellow)}
.side-ad .t2{font-family:Oswald,sans-serif;font-size:17px;color:#e9e9e9}
.side-cap{left:214px;top:628px;width:154px;height:48px;background:var(--light);text-align:center;font-size:7px;padding-top:6px;line-height:11px}
.side-cap b{display:block;font-size:7.5px}
/* main */
.main-title{left:390px;top:302px;font-size:14px}
.main-title b{font-weight:600}
.filter{left:728px;top:302px;width:104px;height:22px;border:1px solid var(--line);color:#bbb;font-size:7.5px;padding:6px 7px}
.card{width:212px;height:106px;background:var(--white)}
.card .head{height:28px;background:var(--light);border-bottom:1px solid var(--line);font-size:8px;font-weight:700;padding:9px 11px;color:#444}
.card .body{height:36px;background:var(--light);font-size:6px;color:#555;padding:8px 10px 0 12px;line-height:9px}
.card .row{height:17px;display:flex;align-items:center;font-size:7px;color:#444;background:var(--light);margin-top:1px}
.card .row .ic{width:22px;height:15px;background:var(--yellow);margin-right:8px;display:flex;align-items:center;justify-content:center}
.card .row:first-of-type{margin-top:2px}
.banner{left:389px;top:574px;width:444px;height:55px;border:1px solid #4aa3d8;background:linear-gradient(90deg,#eaf6fd,#d6ecf8 60%,#b9c2c8);display:flex;align-items:center;padding-left:60px;gap:24px}
.banner .org{font-size:8px;font-weight:700;color:#1d4e89}
.banner .org span{display:block;font-size:17px;color:#2d7fc1;font-weight:700}
.banner .when{font-size:13px;font-weight:700;color:#173a66;line-height:17px}
.view-more{left:499px;top:649px;width:66px;height:24px;background:var(--yellow);font-size:8px;font-weight:700;display:flex;align-items:center;justify-content:center;gap:4px}
/* register */
.register{left:0;top:696px;width:1080px;height:72px;background:linear-gradient(90deg,#1f1f1f,#3a3a3a 50%,#232323);color:var(--white);text-align:center;font-size:13px;line-height:72px}
.register b{font-weight:700}
/* classifieds */
.classifieds{left:0;top:768px;width:1080px;height:223px;background:var(--yellow)}
.cl-title{left:214px;top:795px;font-size:11px;font-weight:700}
.post-ad{left:300px;top:792px;width:71px;height:20px;background:var(--dark);color:var(--white);font-size:8px;font-weight:700;text-align:center;line-height:20px}
.search-more{left:773px;top:792px;width:75px;height:20px;background:var(--dark);color:var(--white);font-size:8px;font-weight:700;text-align:center;line-height:20px}
.cat{width:146px;top:838px}
.cat h4{font-size:8.5px;font-weight:700;padding-bottom:6px;border-bottom:1px solid #8a6e00}
.cat h4 span{color:#9a7c00}
.cat ul{list-style:none;margin-top:8px}
.cat li{font-size:8px;line-height:14.8px}
/* footer */
.footer{left:0;top:991px;width:1080px;height:209px;background:var(--dark)}
.ft-search-wrap{left:434px;top:991px;width:331px;height:44px;background:#2b2b2b}
.ft-search{left:449px;top:1002px;width:172px;height:24px;background:var(--white);color:#888;font-size:7.5px;padding:7px 10px}
.ft-go{left:621px;top:1002px;width:32px;height:24px;background:#555}
.best{left:765px;top:991px;width:83px;height:44px;background:var(--yellow);color:var(--charcoal);font-family:Oswald,sans-serif;font-size:12px;text-align:center;line-height:13px;padding-top:9px}
.testi-h{left:214px;top:1008px;font-size:11px;font-weight:700;color:var(--white)}
.testi-p{left:214px;top:1032px;width:195px;font-size:6.5px;line-height:9.5px;color:#ddd}
.testi-n{left:214px;top:1075px;font-size:6.5px;font-weight:700;color:var(--white)}
.dots{left:215px;top:1099px;display:flex;gap:3px}
.dots i{width:6px;height:6px;border-radius:50%;background:#777}
.dots i.on{background:var(--yellow)}
.ft-links{left:432px;top:1061px;width:418px;font-size:6.5px;line-height:10px;color:#ddd}
.socials{left:432px;top:1092px;display:flex;gap:10px}
.socials i{width:24px;height:20px;background:var(--yellow)}
.ft-rule{left:214px;width:634px;height:1px;background:#444}
.ft-cols{left:214px;top:1143px;width:634px;display:flex;font-size:6.5px;color:#bbb;align-items:center}
.ft-cols div{width:110px;line-height:9px;border-right:1px solid #444;padding-left:2px}
.ft-cols div:last-child{border:none;width:auto;flex:1;padding-left:12px}
.ft-cols b{display:block;font-weight:400;color:var(--yellow);font-size:7px}
.ft-cols .phone{font-size:13px;color:var(--yellow);display:inline;margin-left:4px}
.copy{left:0;top:1183px;width:1080px;text-align:center;font-size:6.5px;color:#ccc}
</style>
</head>
<body>
<div class="abs topbar"></div>
<div class="abs brand">Drone Directory</div>
<div class="abs top-links"><span>Login</span><span>Register</span><span>Share</span><span>EN</span></div>
<div class="abs add-listing"><b>+</b>Add Listing</div>

<div class="abs hero" role="img" aria-label="City street photograph with shop fronts and tall buildings"></div>
<div class="abs search-strip"></div>
<div class="abs search-row">
  <div class="menu"><i></i><i></i><i></i></div>
  <div class="field">Search Keyword</div>
  <div class="field">Search Category</div>
  <div class="field">Search Location</div>
  <div class="go"><svg width="24" height="19" viewBox="0 0 24 19"><circle cx="10" cy="8" r="3.5" fill="none" stroke="#222" stroke-width="1.6"/><path d="M12.5 10.5l4 4" stroke="#222" stroke-width="1.8"/></svg></div>
</div>
<div class="abs alpha">
  <span>A</span><span class="on">B</span><span>C</span><span>D</span><span>E</span><span>F</span><span>G</span><span>H</span><span>I</span><span>J</span><span>K</span><span>L</span><span>M</span><span>N</span><span>O</span><span>P</span><span>Q</span><span>R</span><span>S</span><span>T</span><span>U</span><span>V</span><span>W</span><span>X</span><span>Y</span><span>Z</span><span>0</span><span>1</span><span>2</span><span>3</span><span>4</span><span>5</span><span>6</span><span>7</span><span>8</span><span>9</span>
</div>
<div class="abs hero-title">Drone Directory</div>
<div class="abs hero-sub">Lorem Ipsum is simply dummy text of the printing and typesetting industry</div>

<nav class="abs nav"><a class="on">HOME</a><a>COMPANY</a><a>CUSTOM LINK</a><a>BLOG</a><a>ABOUT US</a><a>CONTACT US</a></nav>
<div class="abs panel"></div>

<div class="abs side-head">BROWSE DIRECTORIES</div>
<ul class="abs side-list">
  <li class="first">Rotor Insights</li><li>Pocketbyte-PersonalTech</li><li>Wide World – Daily News</li><li>Market Value</li><li>SkyvanTerra Australia</li><li>Rotor Insights</li><li>Pocketbyte-PersonalTech</li><li>Wide World – Daily News</li><li>Market Value</li>
</ul>
<div class="abs see-more">›&nbsp;&nbsp;SEE MORE</div>
<div class="abs side-ad"><div class="t1">THE AERIAL SYSTEMS</div><div class="t2">EXPO ASIA 2015</div></div>
<div class="abs side-cap">30 June - 1 July 2015<b>Harborview Convention &amp; Exhibition Centre, Singapore.</b></div>

<div class="abs main-title"><b>Rotor</b> Insights</div>
<div class="abs filter">Filter</div>

<div class="abs card" style="left:390px;top:328px">
  <div class="head">Name of the Product List</div>
  <div class="body">Lorem Ipsum is simply dummy text of the printing and typesetting industry. Lorem Ipsum has been the industry's standard dummy</div>
  <div class="row"><span class="ic"><svg width="8" height="10"><path d="M4 10C1 6 0 4.5 0 3.5a4 4 0 018 0C8 4.5 7 6 4 10z" fill="#222"/><circle cx="4" cy="3.6" r="1.3" fill="#f5c400"/></svg></span># 1234, Street Name, City Name, Country Name</div>
  <div class="row"><span class="ic"><svg width="9" height="7"><rect width="9" height="7" fill="#222"/><path d="M0 0l4.5 4L9 0" stroke="#f5c400" fill="none"/></svg></span>info@companyname.com</div>
</div>
<div class="abs card" style="left:620px;top:328px">
  <div class="head">Name of the Product List</div>
  <div class="body">Lorem Ipsum is simply dummy text of the printing and typesetting industry. Lorem Ipsum has been the industry's standard dummy</div>
  <div class="row"><span class="ic"><svg width="8" height="10"><path d="M4 10C1 6 0 4.5 0 3.5a4 4 0 018 0C8 4.5 7 6 4 10z" fill="#222"/><circle cx="4" cy="3.6" r="1.3" fill="#f5c400"/></svg></span># 1234, Street Name, City Name, Country Name</div>
  <div class="row"><span class="ic"><svg width="9" height="7"><rect width="9" height="7" fill="#222"/><path d="M0 0l4.5 4L9 0" stroke="#f5c400" fill="none"/></svg></span>info@companyname.com</div>
</div>
<div class="abs card" style="left:390px;top:450px">
  <div class="head">Name of the Product List</div>
  <div class="body">Lorem Ipsum is simply dummy text of the printing and typesetting industry. Lorem Ipsum has been the industry's standard dummy</div>
  <div class="row"><span class="ic"><svg width="8" height="10"><path d="M4 10C1 6 0 4.5 0 3.5a4 4 0 018 0C8 4.5 7 6 4 10z" fill="#222"/><circle cx="4" cy="3.6" r="1.3" fill="#f5c400"/></svg></span># 1234, Street Name, City Name, Country Name</div>
  <div class="row"><span class="ic"><svg width="9" height="7"><rect width="9" height="7" fill="#222"/><path d="M0 0l4.5 4L9 0" stroke="#f5c400" fill="none"/></svg></span>info@companyname.com</div>
</div>
<div class="abs card" style="left:620px;top:450px">
  <div class="head">Name of the Product List</div>
  <div class="body">Lorem Ipsum is simply dummy text of the printing and typesetting industry. Lorem Ipsum has been the industry's standard dummy</div>
  <div class="row"><span class="ic"><svg width="8" height="10"><path d="M4 10C1 6 0 4.5 0 3.5a4 4 0 018 0C8 4.5 7 6 4 10z" fill="#222"/><circle cx="4" cy="3.6" r="1.3" fill="#f5c400"/></svg></span># 1234, Street Name, City Name, Country Name</div>
  <div class="row"><span class="ic"><svg width="9" height="7"><rect width="9" height="7" fill="#222"/><path d="M0 0l4.5 4L9 0" stroke="#f5c400" fill="none"/></svg></span>info@companyname.com</div>
</div>

<div class="abs banner" role="img" aria-label="Event advertisement banner with drone imagery">
  <div class="org">Skyline Events presents<span>DRONE SUMMIT</span></div>
  <div class="when">28 - 29 OCTOBER, 2014<br>Brisbane, QLD, Australia</div>
</div>
<div class="abs view-more"><svg width="8" height="8"><rect x=".5" y=".5" width="7" height="7" fill="none" stroke="#222"/><path d="M4 2v4M2 4h4" stroke="#222"/></svg>View More</div>

<div class="abs register" role="img" aria-label="Dark desk photograph behind the register call"><b>REGISTER</b> NOW</div>

<div class="abs classifieds"></div>
<div class="abs cl-title">CLASSIFIEDS</div>
<div class="abs post-ad">+ Post Your Ad</div>
<div class="abs search-more">SEARCH MORE</div>
<div class="abs cat" style="left:214px"><h4>ADVERTISING <span>(1090)</span></h4><ul><li>Antiques (23)</li><li>Books (31)</li><li>Cars &amp; Motorcycles (45)</li><li>Computers &amp; Tablets (234)</li><li>Creative &amp; Digitals (47)</li><li>Fashion (51)</li><li>Fitness &amp; Sports (34)</li></ul></div>
<div class="abs cat" style="left:375px"><h4>ECOMMERCE <span>(10390)</span></h4><ul><li>Antiques (23)</li><li>Books (31)</li><li>Cars &amp; Motorcycles (45)</li><li>Computers &amp; Tablets (234)</li><li>Creative &amp; Digitals (47)</li><li>Fashion (51)</li><li>Fitness &amp; Sports (34)</li></ul></div>
<div class="abs cat" style="left:539px"><h4>EDUCATION <span>(1034)</span></h4><ul><li>Antiques (23)</li><li>Books (31)</li><li>Cars &amp; Motorcycles (45)</li><li>Computers &amp; Tablets (234)</li><li>Creative &amp; Digitals (47)</li><li>Fashion (51)</li><li>Fitness &amp; Sports (34)</li></ul></div>
<div class="abs cat" style="left:702px"><h4>SPORTS <span>(190)</span></h4><ul><li>Antiques (23)</li><li>Books (31)</li><li>Cars &amp; Motorcycles (45)</li><li>Computers &amp; Tablets (234)</li><li>Creative &amp; Digitals (47)</li><li>Fashion (51)</li><li>Fitness &amp; Sports (34)</li></ul></div>

<footer class="abs footer"></footer>
<div class="abs ft-search-wrap"></div>
<div class="abs ft-search">Enter Search Keyword</div>
<div class="abs ft-go"><svg width="32" height="24"><circle cx="14" cy="10" r="4" fill="none" stroke="#f5c400" stroke-width="1.6"/><path d="M17 13l4 4" stroke="#f5c400" stroke-width="2"/></svg></div>
<div class="abs best">BEST<br>RATES</div>
<div class="abs testi-h">Testimonials</div>
<div class="abs testi-p">Lorem Ipsum is simply dummy text of the printing and typesetting industry. Lorem Ipsum has been the industry's standard dummy text ever since the 1500s, when an unknown printer took a galley</div>
<div class="abs testi-n">Lorem Ipsum, Company</div>
<div class="abs dots"><i></i><i class="on"></i><i></i><i></i><i></i></div>
<div class="abs ft-links">Advertise with Us | About us | Contact us | Digital Careers Exhibitions | Distribution Report | Privacy Policy | Terms of Service Fashion Weddings Education Gadgets Interiors Sports Cars Travel Health Food Youngmoms</div>
<div class="abs socials"><i aria-label="Social link"></i><i aria-label="Social link"></i><i aria-label="Social link"></i></div>
<div class="abs ft-rule" style="top:1134px"></div>
<div class="abs ft-cols">
  <div>Send Us<b>Your Feedback</b></div>
  <div>Recent<b>News</b></div>
  <div>Blog<b>Updates</b></div>
  <div>Advertise<b>With Us</b></div>
  <div>Queries<br>Call Us <b class="phone">123 456 78900</b></div>
</div>
<div class="abs ft-rule" style="top:1166px"></div>
<div class="abs copy">All rights reserved © 2014 Company Name</div>
</body>
</html>
```